Bright Harbor Family Law Firm Website Renovation

We need a website redesign in SquareSpace that is more modern, user friendly, on brand, less cluttered, easier to navigate, conveys clearly what our services are, and has clear, visible calls to action.

We would like to hire and work with the winning designer to complete the remaining pages of the site.
Updates

Gathering more feedback

Target Market(s)

Couples looking for divorce representation or mediation who have a conscious, progressive mindset. They are self-aware and personal development plays an important role in their lives. They want an amicable interaction and aspire to have a healthy relationship after divorce.

Age range: 30-60
Income 100K+ household

Industry/Entity Type

Family Law

Font styles to use
Sans Serif

Colors
85acd3
33a6d7
50c0af
a0cd3a

Requirements
Must have
• Please see attached doc for full creative brief details.

"Changing the way people divorce" on top of site.
Images that show happy clients and that represent males and females. Diversity inclusion is also be important.
We are looking for warm, welcoming design and imagery.
Should not have
• Not heavily attorney focused.
Please see attached brief for full description.

```html
<!DOCTYPE html>
<html lang="en">
<head>
<meta charset="utf-8">
<title>Bright Harbor Family Law &amp; Mediation</title>
<link href="https://fonts.googleapis.com/css2?family=Lato:wght@300;400;700;900&family=Crimson+Text:wght@400;600&display=swap" rel="stylesheet">
<style>
:root{
  --blue:#33a6d7;
  --sky:#85acd3;
  --teal:#50c0af;
  --lime:#a0cd3a;
  --ink:#1d1d1d;
  --text:#555;
  --mist:#eefbfb;
  --night:#0e0e0e;
  --line:#ddd;
}
*{box-sizing:border-box;margin:0;padding:0}
html,body{width:1200px;height:4953px;overflow:hidden;background:#fff}
body{position:relative;font-family:"Crimson Text",Georgia,serif;color:var(--text)}
section,header,footer{position:absolute;left:0;width:1200px}
.abs{position:absolute}
.btn{position:absolute;display:flex;align-items:center;justify-content:center;font-family:"Lato",Arial,sans-serif;font-weight:700;font-size:15px;letter-spacing:.5px;text-transform:uppercase;color:#fff;background:var(--blue);box-shadow:0 3px 6px rgba(0,0,0,.2)}
.btn.light{background:#fff;color:var(--ink)}
/* header */
.site-header{top:0;height:106px}
.brand{left:150px;top:10px;width:130px;text-align:center;font-family:"Lato",Arial,sans-serif;color:#3b3b3b}
.brand-dot{width:46px;height:46px;border-radius:50%;background:var(--teal);margin:0 auto 6px}
.brand-name{font-size:11px;letter-spacing:2px;line-height:1.25;text-transform:uppercase}
.topbar{left:383px;top:0;width:817px;height:53px;background:#f0f0f0}
.topbar .call{position:absolute;left:185px;top:16px;font-size:16px;color:#333}
.topbar .btn{left:525px;top:8px;width:136px;height:36px;font-size:15px;box-shadow:none}
.nav{left:430px;top:70px;display:flex;font-size:17px;color:#333}
.nav span{padding:0 26px;border-left:1px solid #888;line-height:22px}
.nav span:first-child{border:none}
.search{left:1012px;top:66px;width:30px;height:30px;border-radius:50%;background:var(--blue)}
/* hero */
.hero{top:106px;height:498px}
.hero-photo{position:absolute;inset:0;background:linear-gradient(100deg,#514743 0%,#8e8077 45%,#d6cec6 75%,#efebe6 100%)}
.hero h1{position:absolute;left:156px;top:90px;font-family:"Lato",Arial,sans-serif;font-weight:700;font-size:46px;line-height:48px;color:#fff;text-transform:uppercase}
.hero p{position:absolute;left:158px;top:240px;width:400px;font-family:"Lato",Arial,sans-serif;font-weight:300;font-size:23px;line-height:29px;color:#fff}
.hero .slider{position:absolute;left:158px;top:365px;width:85px;height:2px;background:rgba(255,255,255,.6)}
.hero .slider::before{content:"";position:absolute;left:0;top:-4px;width:10px;height:10px;border-radius:50%;background:var(--blue)}
/* intro */
.intro{top:604px;height:600px}
.intro h2{position:absolute;left:157px;top:78px;width:420px;font-family:"Lato",Arial,sans-serif;font-weight:700;font-size:34px;line-height:40px;color:var(--ink)}
.intro p{position:absolute;left:158px;width:360px;font-size:15px;line-height:22px;color:#666}
.advocate{position:absolute;left:606px;top:65px;width:436px;height:471px;background:#fff;box-shadow:0 2px 10px rgba(0,0,0,.15)}
.advocate .head{position:absolute;left:11px;top:11px;width:414px;height:92px;background:var(--blue);text-align:center;color:#fff}
.advocate .head b{display:block;font-family:"Lato",Arial,sans-serif;font-weight:400;font-size:34px;margin-top:16px}
.advocate .head small{font-family:"Lato",Arial,sans-serif;font-size:13px;letter-spacing:.4px}
.advocate .frame{position:absolute;left:11px;top:103px;width:414px;height:355px;border:2px solid var(--lime);border-top:none}
.field{position:absolute;height:42px;background:#f0f0f0;border:1px solid #ddd;font-size:13px;color:#666;padding:13px 12px}
.advocate .btn{left:113px;top:397px;width:210px;height:42px}
.rule{position:absolute;left:158px;top:600px;width:885px;height:1px;background:var(--line)}
.badge{position:absolute;top:640px;height:120px;border-radius:6px}
/* services */
.services{top:1461px;height:587px;background:var(--mist)}
.services h2{position:absolute;left:0;width:1200px;top:58px;text-align:center;font-family:"Lato",Arial,sans-serif;font-weight:700;font-size:35px;color:var(--ink)}
.ring{position:absolute;left:468px;top:115px;width:265px;height:265px;border-radius:50%;background:radial-gradient(circle,#fff 30%,#d5f0ee 70%,var(--mist) 72%)}
.axis{position:absolute;left:600px;top:128px;width:1px;height:290px;background:#bde0e6}
.axis::before,.axis::after{content:"";position:absolute;left:-4px;width:9px;height:9px;border-radius:50%;background:var(--blue)}
.axis::before{top:-4px}.axis::after{bottom:-4px}
.svc{position:absolute;top:131px;width:330px;text-align:center}
.svc .icon{width:154px;height:154px;border-radius:50%;background:var(--lime);margin:0 auto;display:flex;align-items:center;justify-content:center}
.svc h3{font-family:"Lato",Arial,sans-serif;font-weight:700;font-size:21px;line-height:27px;color:#222;margin-top:22px}
.svc p{font-size:15px;line-height:21px;color:#666;margin:14px auto 0;width:300px}
.services .btn{left:532px;top:480px;width:136px;height:40px}
/* cta band */
.cta{top:2048px;height:158px;background:var(--teal)}
.cta h2{position:absolute;left:161px;top:56px;font-family:"Lato",Arial,sans-serif;font-weight:400;font-size:36px;color:#fff}
.cta .btn{left:683px;top:56px;width:360px;height:46px;font-size:14px}
/* video */
.video{top:2206px;height:500px;background:linear-gradient(180deg,#3d4347 0%,#5b5d58 45%,#34332c 100%)}
.video .label{position:absolute;left:0;width:1200px;top:135px;text-align:center;font-family:"Lato",Arial,sans-serif;font-size:16px;letter-spacing:1px;color:#fff}
.video .play{position:absolute;left:558px;top:172px}
.video h2{position:absolute;left:0;width:1200px;top:280px;text-align:center;font-family:"Lato",Arial,sans-serif;font-weight:400;font-size:36px;line-height:43px;color:#fff}
/* testimonial */
.testimonial{top:2706px;height:448px}
.quote-mark{position:absolute;font-family:"Lato",Arial,sans-serif;font-weight:900;font-size:110px;line-height:1;color:var(--lime)}
.testimonial blockquote{position:absolute;left:162px;top:88px;width:880px;font-size:22px;line-height:32px;color:#333;text-indent:60px}
.testimonial cite{position:absolute;left:164px;top:280px;font-family:"Lato",Arial,sans-serif;font-style:normal;font-size:13px;color:#444}
.testimonial .btn{left:158px;top:337px;width:285px;height:44px}
/* team */
.team{top:3154px;height:529px;background:var(--teal)}
.team h2{position:absolute;left:0;width:1150px;top:50px;text-align:center;font-family:"Lato",Arial,sans-serif;font-weight:400;font-size:36px;color:#fff}
.member{position:absolute;top:125px;width:210px;font-family:"Lato",Arial,sans-serif}
.member .photo{width:210px;height:206px;border:4px solid #fff;background:linear-gradient(180deg,#c9c4bc,#8a8178)}
.member h3{font-weight:700;font-size:18px;color:#fff;margin-top:16px;text-transform:uppercase}
.member small{display:block;font-size:11px;color:#fff;text-transform:uppercase;margin-top:2px;white-space:nowrap}
.member .btn{position:relative;width:136px;height:38px;margin-top:26px;font-size:13px}
.arrow{position:absolute;top:208px;width:42px;height:42px;border-radius:50%;background:#fff;display:flex;align-items:center;justify-content:center}
/* map + contact */
.map{top:3683px;height:394px;background:linear-gradient(135deg,#ececec,#dcdcdc)}
.night{top:4077px;height:876px;background:var(--night)}
.contact-info{position:absolute;left:233px;top:3913px;width:284px;height:414px;background:var(--blue);color:#fff;font-family:"Lato",Arial,sans-serif;padding:28px 26px}
.contact-info h3{font-weight:400;font-size:25px;margin-bottom:18px}
.contact-info .row{display:flex;gap:10px;font-size:14px;line-height:21px;margin-bottom:14px}
.contact-info h4{font-weight:400;font-size:23px;margin:20px 0 12px}
.social{display:flex;gap:9px}
.social i{width:40px;height:40px;border:2px solid #fff;border-radius:50%}
.message{position:absolute;left:517px;top:3913px;width:448px;height:414px;background:#fff;font-family:"Lato",Arial,sans-serif;padding:26px 44px}
.message h3{font-weight:700;font-size:24px;color:#222}
.message .ln{position:absolute;left:44px;width:360px;border-bottom:1px solid #ccc;font-size:12px;color:#666;padding-bottom:6px}
.captcha{position:absolute;left:44px;top:300px;display:flex;align-items:center;gap:10px;font-size:11px;color:#444}
.captcha i{width:18px;height:18px;border:1px solid #aaa}
.message .btn{left:275px;top:293px;width:135px;height:40px}
/* footer */
.site-footer{top:4327px;height:626px;text-align:center;color:#fff}
.site-footer h2{position:absolute;left:0;width:1200px;top:42px;font-family:"Lato",Arial,sans-serif;font-weight:400;font-size:25px}
.site-footer p{position:absolute;left:235px;top:95px;width:730px;font-size:14px;line-height:21px;color:#ddd}
.foot-brand{position:absolute;left:480px;top:190px;width:240px;font-family:"Lato",Arial,sans-serif;color:#777;text-transform:uppercase}
.foot-brand i{display:block;width:120px;height:120px;border-radius:50%;background:#1f6d63;margin:0 auto 12px}
.foot-brand b{font-weight:400;font-size:21px;letter-spacing:5px;line-height:25px;display:block}
.foot-brand small{font-size:11px;letter-spacing:3px}
.foot-nav{position:absolute;left:0;width:1200px;top:448px;font-size:15px;color:#fff}
.foot-nav span{margin:0 10px}
.pay{position:absolute;left:448px;top:486px;display:flex;gap:8px;font-family:"Lato",Arial,sans-serif}
.pay span{height:26px;padding:0 8px;background:#fff;color:#1c3d7a;font-weight:700;font-size:14px;line-height:26px;border-radius:3px}
.copy{position:absolute;left:0;width:1200px;top:540px;font-size:13px;color:#ddd}
.top-link{position:absolute;left:948px;top:536px;font-size:14px;color:#ddd}
</style>
</head>
<body>

<header class="site-header">
  <div class="abs brand"><div class="brand-dot"></div><div class="brand-name">Bright Harbor<br>Family Law</div></div>
  <div class="abs topbar">
    <div class="call">&#9990; Call to learn how we can help (555) 014-2290</div>
    <div class="btn">+ Sign Up</div>
  </div>
  <nav class="abs nav"><span>Home</span><span>Services</span><span>About</span><span>Contact</span><span>FAQ</span><span>Blog</span></nav>
  <div class="abs search"><svg width="30" height="30" viewBox="0 0 30 30"><circle cx="14" cy="14" r="5" fill="none" stroke="#fff" stroke-width="2"/><line x1="18" y1="18" x2="21" y2="21" stroke="#fff" stroke-width="2"/></svg></div>
</header>

<section class="hero">
  <div class="hero-photo" role="img" aria-label="Photo of parents arguing in a living room while a young girl covers her ears"></div>
  <h1>Bright Harbor<br>Family - Law &amp;<br>Mediation</h1>
  <p>Collaborative divorce mediation or legal representation with strength and integrity.</p>
  <div class="slider"></div>
  <div class="btn" style="left:158px;top:378px;width:211px;height:42px">Make Appointment</div>
</section>

<section class="intro">
  <h2>Efficient and positive<br>family legal transitions<br>without costly,<br>painful legal battles.</h2>
  <p style="top:250px">Traditionally, divorcing couples had two options: hire lawyers and go to battle, or avoid divorce professionals.</p>
  <p style="top:330px">Many people don't want to add unnecessary financial and emotional costs to their divorce, but they need professional help to ensure they come away with a good parenting plan and fair financial outcomes.</p>
  <div class="btn" style="left:158px;top:460px;width:210px;height:42px">Read Continue</div>

  <form class="advocate">
    <div class="head"><b>Need an Advocate</b><small>REQUEST A FREE CONSULTATION</small></div>
    <div class="frame"></div>
    <div class="field" style="left:30px;top:134px;width:186px">Name:</div>
    <div class="field" style="left:222px;top:134px;width:186px">Email:</div>
    <div class="field" style="left:30px;top:187px;width:186px">Phone:</div>
    <div class="field" style="left:222px;top:187px;width:186px">County of case:</div>
    <div class="field" style="left:30px;top:240px;width:378px">Are you a new client?</div>
    <div class="field" style="left:30px;top:293px;width:378px;height:95px">Message:</div>
    <div class="btn">Make Appointment</div>
  </form>

  <div class="rule"></div>
  <div class="badge" style="left:226px;width:130px;background:#1f5f8f" role="img" aria-label="Attorney rating badge"></div>
  <div class="badge" style="left:388px;width:90px;height:90px;top:655px;border-radius:50%;background:#e8943a" role="img" aria-label="Rated lawyer badge"></div>
  <div class="badge" style="left:512px;width:138px;background:#5a3d8c" role="img" aria-label="Highly recommended badge"></div>
  <div class="badge" style="left:685px;width:92px;height:92px;top:665px;border-radius:50%;background:#d8a93a" role="img" aria-label="Award medal"></div>
  <div class="badge" style="left:815px;width:160px;background:#f2f2f2" role="img" aria-label="Corporate sponsor badge for a children's charity"></div>
</section>

<section class="services">
  <h2>OUR SERVICES</h2>
  <div class="ring"></div>
  <div class="axis"></div>
  <div class="svc" style="left:231px">
    <div class="icon"><svg width="80" height="70" viewBox="0 0 80 70" fill="#fff"><rect x="10" y="34" width="60" height="6"/><rect x="22" y="40" width="6" height="24"/><rect x="52" y="40" width="6" height="24"/><circle cx="22" cy="12" r="7"/><circle cx="58" cy="12" r="7"/><circle cx="40" cy="16" r="6"/></svg></div>
    <h3>BRIGHT HARBOR<br>MEDIATION</h3>
    <p>Our unique attorney-mediated process can deliver you and your family through divorce and into a healthy new life.</p>
  </div>
  <div class="svc" style="left:600px">
    <div class="icon"><svg width="70" height="80" viewBox="0 0 70 80" fill="#fff"><circle cx="28" cy="14" r="11"/><path d="M10 60 q0-28 18-28 q18 0 18 28z"/><rect x="44" y="40" width="3" height="30"/><rect x="34" y="44" width="24" height="3"/><path d="M32 58 l4-10 l4 10z M52 58 l4-10 l4 10z"/></svg></div>
    <h3>BRIGHT HARBOR<br>LAWYER</h3>
    <p>Our attorneys are there when you need the protection of a mature, conscious advocate</p>
  </div>
  <div class="btn">View Details</div>
</section>

<section class="cta">
  <h2>Get your questions answered</h2>
  <div class="btn light">Schedule a Free Information Call</div>
</section>

<section class="video" role="img" aria-label="Video still of a family walking together across a mountain meadow">
  <div class="label">PLAY VIDEO</div>
  <svg class="play" width="84" height="84" viewBox="0 0 84 84"><circle cx="42" cy="42" r="39" fill="none" stroke="#fff" stroke-width="3"/><path d="M35 29 L56 42 L35 55z" fill="#fff"/></svg>
  <h2>LEARN HOW WE ARE CHANGING<br>THE WAY PEOPLE DIVORCE</h2>
</section>

<section class="testimonial">
  <div class="quote-mark" style="left:155px;top:58px">&ldquo;</div>
  <blockquote>I am so grateful for my experience with Bright Harbor Family Law &amp; Mediation. I learned so much about myself and my capacity to love, grieve, and heal. You were so great at facilitating our difficult conversations, helping both of us feel validated, and coaching us on how to work well with each other moving forward in our new co-parenting relationship.</blockquote>
  <div class="quote-mark" style="left:610px;top:215px">&rdquo;</div>
  <cite>-DIVORCE MEDIATION CLIENT</cite>
  <div class="btn">Read More Testimonials</div>
</section>

<section class="team">
  <h2>OUR TEAM</h2>
  <div class="arrow" style="left:132px"><svg width="14" height="14" viewBox="0 0 14 14"><path d="M9 2 L4 7 L9 12" fill="none" stroke="var(--teal)" stroke-width="2.5"/></svg></div>
  <div class="arrow" style="left:1019px"><svg width="14" height="14" viewBox="0 0 14 14"><path d="M5 2 L10 7 L5 12" fill="none" stroke="var(--teal)" stroke-width="2.5"/></svg></div>
  <div class="member" style="left:158px"><div class="photo" role="img" aria-label="Portrait of partner attorney"></div><h3>Mark Linden</h3><small>Partner Attorney/Mediator</small><div class="btn light">View Profile</div></div>
  <div class="member" style="left:383px"><div class="photo" role="img" aria-label="Portrait of partner attorney"></div><h3>Paul Reyes</h3><small>Partner Attorney/Mediator</small><div class="btn light">View Profile</div></div>
  <div class="member" style="left:608px"><div class="photo" role="img" aria-label="Portrait of senior attorney"></div><h3>Claire Whitman</h3><small>Senior Attorney</small><div class="btn light">View Profile</div></div>
  <div class="member" style="left:833px"><div class="photo" role="img" aria-label="Portrait of associate attorney"></div><h3>Nora Ashby</h3><small>Associate Attorney/Mediator</small><div class="btn light">View Profile</div></div>
</section>

<section class="map" role="img" aria-label="Street map showing the office location"></section>
<section class="night"></section>

<div class="contact-info">
  <h3>Contact Us</h3>
  <div class="row"><span>&#9679;</span><span>Bright Harbor Family Law &amp; Mediation LLC 1420 Larkspur Avenue, Unit 9 Fernvale, Westmark 00417</span></div>
  <div class="row"><span>&#9990;</span><span>1+ (555) 014-2290</span></div>
  <div class="row"><span>&#9993;</span><span>info@brightharborlaw.com</span></div>
  <h4>Follow Us On</h4>
  <div class="social"><i></i><i></i><i></i></div>
</div>

<form class="message">
  <h3>Send a Message</h3>
  <div class="ln" style="top:110px">Name:</div>
  <div class="ln" style="top:157px">Email:</div>
  <div class="ln" style="top:230px">Message:</div>
  <div class="captcha"><i></i>I'm not a robot</div>
  <div class="btn">Submit</div>
</form>

<footer class="site-footer">
  <h2>We are proud to serve your family.</h2>
  <p>Bright Harbor Family Law &amp; Mediation LLC currently serves the legal needs of Westmark residents (including same-sex and other alternative families) in Fernvale County, Alder County, Birchwood County, Stonebrook County, Cedar County, Willow County, and Maple County.</p>
  <div class="foot-brand"><i></i><b>Bright Harbor<br>Family</b><small>Law &amp; Mediation</small></div>
  <div class="foot-nav">Home<span>&bull;</span>Services<span>&bull;</span>About<span>&bull;</span>Contact<span>&bull;</span>FAQ<span>&bull;</span>Blog<span>&bull;</span>Resources<span>&bull;</span>Testimonials</div>
  <div class="pay"><span>PayWell</span><span>Card</span><span>Card</span><span>Card</span><span>Card</span></div>
  <div class="copy">&copy; 2020 Bright Harbor Family Law &amp; Mediation. All rights reserved.</div>
  <div class="top-link">&uarr; Back To Top</div>
</footer>

</body>
</html>
```